Virtual Reality company needs business card design

We would like a business card that is simple and memorable. Telvani is a global startup based in San Francisco and Singapore. We are a company with products and services for both the B2B and B2C audiences. We develop platforms with educational content, and allow people to interact with the content in a virtual environment setting. Our end user will be able to learn and 'see' the world's culture and history from the comfort of their home. The business card will primarily be used for B2B audience and not overly corporate in image, but requires a universal appeal - evoking sense of friendliness and innovation. Attached is our logo with two color options. We are open to single-sided or double-sided designs. EPS/AI files will be provided to winning designer at final design stage.

Other text that will be included in card: (Name), (Address), (Tel), (Email), (Website)

Include option of having TWO QR codes which are 0.5 inch x 0.5 inch each
Updates

Dear Designers,

Thank you for your submissions. We are currently in process of reviewing your designs and will make a decision in the next few days.

Regards,
Telvani

Industry/Entity Type

Environment

Font styles to use
Serif
Sans Serif

Requirements
Must have
• Spacing for Name, Address, Tel, Email, Web address
Should not have
• Limit the number of colors utilised.

```html
<!DOCTYPE html>
<html lang="en">
<head>
<meta charset="utf-8">
<title>Telvani Business Card</title>
<link rel="stylesheet" href="https://fonts.googleapis.com/css2?family=Arimo:wght@400;700&display=swap">
<style>
  :root {
    --bg: #d9d9d9;
    --card: #f7f7f7;
    --brand-blue: #3b96cc;
    --ink: #2f2f2f;
    --ink-soft: #555555;
    --band-dark: #3a3a3a;
    --mark-faint: #dcdcdc;
  }
  * { box-sizing: border-box; margin: 0; padding: 0; }
  html, body {
    width: 1200px; height: 800px; overflow: hidden;
    background: var(--bg);
    font-family: "Arimo", Arial, sans-serif;
  }
  .stage {
    width: 1200px; height: 800px;
    display: flex; align-items: center; justify-content: center; gap: 40px;
  }
  .card {
    position: relative;
    width: 540px; height: 309px;
    background: var(--card);
    overflow: hidden;
    box-shadow: 0 2px 6px rgba(0,0,0,0.15);
  }

  /* Front side */
  .card-front .brand-block {
    position: absolute; left: 50%; top: 50%;
    transform: translate(-50%, -50%);
    text-align: left;
  }
  .card-front .web-address {
    font-size: 19px; color: var(--ink-soft);
    margin-left: 70px; letter-spacing: 0.3px;
  }
  .brand-name {
    display: flex; align-items: center; gap: 10px;
    color: var(--brand-blue); font-weight: 400; line-height: 1;
  }
  .brand-name .brand-dot {
    width: 0.5em; height: 0.5em; border-radius: 50%;
    background: var(--brand-blue);
  }
  .card-front .brand-name { font-size: 84px; }

  /* Back side */
  .card-back .identity {
    position: absolute; left: 40px; top: 150px;
  }
  .person-name { font-size: 24px; color: var(--ink); letter-spacing: 0.5px; margin-left: 30px; }
  .person-role { font-size: 15px; color: var(--ink); margin-left: 30px; }
  .card-back .brand-name { font-size: 54px; margin-top: 4px; }
  .divider {
    position: absolute; left: 296px; top: 92px;
    width: 2px; height: 135px; background: var(--brand-blue);
  }
  .faint-mark {
    position: absolute; left: 330px; top: 40px;
    width: 190px; height: 190px; border-radius: 50%;
    background: var(--mark-faint); opacity: 0.6;
  }
  .contact {
    position: absolute; left: 340px; top: 92px;
    font-size: 14px; line-height: 1.25; color: var(--ink-soft);
  }
  .contact .address { margin-bottom: 10px; }
  .contact .label { color: var(--brand-blue); }
  .contact dd { color: var(--ink); }
  .contact .row { display: flex; gap: 4px; }
  .bands { position: absolute; left: 0; bottom: 0; width: 540px; height: 60px; }
</style>
</head>
<body>
<main class="stage">
  <section class="card card-front" aria-label="Card front">
    <div class="brand-block">
      <p class="web-address">yourwebaddress@com</p>
      <p class="brand-name">Telvani<span class="brand-dot"></span></p>
    </div>
  </section>

  <section class="card card-back" aria-label="Card back">
    <div class="faint-mark" aria-hidden="true"></div>
    <div class="identity">
      <p class="person-name">YOUR NAME</p>
      <p class="person-role">Company Position</p>
      <p class="brand-name">Telvani<span class="brand-dot"></span></p>
    </div>
    <div class="divider"></div>
    <dl class="contact">
      <div class="address">
        <p>111 Your Street Address</p>
        <p>206 Town, CT 00000</p>
      </div>
      <div class="row"><dt class="label">E:</dt><dd>youremail@domain.com</dd></div>
      <div class="row"><dt class="label">P:</dt><dd>111-222-444</dd></div>
      <div class="row"><dt class="label">F:</dt><dd>111-222-333</dd></div>
    </dl>
    <svg class="bands" viewBox="0 0 540 60" aria-hidden="true">
      <polygon points="0,44 210,42 230,50 230,60 0,60" fill="var(--brand-blue)"/>
      <polygon points="220,42 540,8 540,60 240,60 240,50" fill="var(--band-dark)"/>
    </svg>
  </section>
</main>
</body>
</html>
```